Law Firm in Texas in need of new letterhead

Law Firm in Fort Worth, TX, USA named "Pell & Whitcombe, Attorneys-At-Law, LLP." This is a general practice law firm that mostly does Family Law and Criminal Defense work.

We are looking for a new letterhead that has a "classical" appeal, with modern elements.

Any color combination is fine, but please note that we do fax many documents, so the design must be clearly legible in Black and White.

We would like our letterhead to project a sense of professionalism, integrity, and ability.

Target Market(s)

Letterhead will be for correspondence generally with other attorneys and clients.

Industry/Entity Type

Law Firm

Logo Text

Pell & Whitcombe, Attorneys-At-Law, LLP.

Logo styles of interest
Pictorial/Combination Logo
Wordmark Logo
Lettermark Logo
Requirements
Nice to have
• Although not necessary, a "Texas Star" that is incorporated into the design would be a nice touch.
Should not have
• Colors that do not convert to B&W easily

```html
<!DOCTYPE html>
<html lang="en">
<head>
<meta charset="utf-8">
<title>Pell &amp; Whitcombe – Letterhead</title>
<link rel="stylesheet" href="https://fonts.googleapis.com/css2?family=Questrial&display=swap">
<style>
  :root {
    --backdrop: #e4e5e7;
    --paper: #ffffff;
    --brand-blue: #2e5d87;
    --ink: #2b2b2b;
    --ink-soft: #555a60;
    --signature-tone: #c9d3e6;
  }
  html, body {
    margin: 0;
    padding: 0;
    width: 1200px;
    height: 827px;
    overflow: hidden;
    background: var(--backdrop);
  }
  .canvas {
    position: relative;
    width: 1200px;
    height: 827px;
  }
  .letterhead {
    position: absolute;
    left: 322px;
    top: 20px;
    width: 556px;
    height: 787px;
    background: var(--paper);
    box-shadow: 0 2px 10px rgba(0,0,0,0.12);
    box-sizing: border-box;
  }
  .masthead {
    position: absolute;
    top: 50px;
    right: 56px;
    display: flex;
    align-items: center;
    gap: 8px;
    color: var(--brand-blue);
  }
  .masthead__mark {
    width: 12px;
    height: 12px;
    background: var(--brand-blue);
  }
  .masthead__name {
    font-family: "Questrial", sans-serif;
    font-weight: 400;
    font-size: 20px;
    line-height: 1;
    color: var(--brand-blue);
  }
  .letter-body {
    position: absolute;
    top: 162px;
    left: 70px;
    width: 400px;
    font-family: "Questrial", sans-serif;
    font-size: 8.6px;
    line-height: 1.55;
    color: var(--ink);
    text-align: justify;
  }
  .letter-body p {
    margin: 0 0 14px;
  }
  .sign-off {
    position: absolute;
    top: 500px;
    right: 56px;
    display: flex;
    align-items: flex-start;
    gap: 18px;
  }
  .signature {
    width: 110px;
    height: 40px;
    background: var(--signature-tone);
    border-radius: 4px;
  }
  .sign-off__text {
    font-family: "Questrial", sans-serif;
    font-size: 8.6px;
    color: var(--ink-soft);
    line-height: 1.6;
  }
  .sign-off__name {
    font-family: "Questrial", sans-serif;
    font-size: 10px;
    color: var(--ink);
  }
  .footer {
    position: absolute;
    right: 56px;
    left: 56px;
    top: 688px;
    text-align: right;
    color: var(--brand-blue);
    font-family: "Questrial", sans-serif;
  }
  .footer__firm {
    font-size: 7.6px;
    letter-spacing: 0.4px;
    text-transform: uppercase;
  }
  .footer__contact {
    font-size: 7.2px;
    margin-top: 3px;
  }
  .footer__contact b {
    color: var(--ink);
  }
  .footer__rule {
    height: 1px;
    background: var(--brand-blue);
    margin-top: 8px;
  }
</style>
</head>
<body>
<main class="canvas">
  <article class="letterhead">
    <header class="masthead">
      <span class="masthead__mark" aria-hidden="true"></span>
      <span class="masthead__name">Pell &amp; Whitcombe</span>
    </header>

    <section class="letter-body">
      <p>Lorem ipsum dolor sit amet, consectetur adipiscing elit, sed do eiusmod tempor incididunt ut labore et dolore magna aliqua. Ut enim ad minim veniam, quis nostrud exercitation ullamco laboris nisi ut aliquip ex ea commodo consequat. Duis aute irure dolor in reprehenderit in voluptate velit esse cillum dolore eu fugiat nulla pariatur. Excepteur sint occaecat cupidatat non proident, sunt in culpa qui officia deserunt mollit anim id est laborum.</p>
      <p>Lorem ipsum dolor sit amet, consectetur adipiscing elit, sed do eiusmod tempor incididunt ut labore et dolore magna aliqua. Ut enim ad minim veniam, quis nostrud exercitation ullamco laboris nisi ut aliquip ex ea commodo consequat.</p>
      <p>Lorem ipsum dolor sit amet, consectetur adipiscing elit, sed do eiusmod tempor incididunt ut labore et dolore magna aliqua. Ut enim ad minim veniam, quis nostrud exercitation ullamco laboris nisi ut aliquip ex ea commodo consequat.</p>
      <p>Lorem ipsum dolor sit amet, consectetur adipiscing elit, sed do eiusmod tempor incididunt ut labore et dolore magna aliqua. Ut enim ad minim veniam, quis nostrud exercitation ullamco laboris nisi ut aliquip ex ea commodo consequat. Duis aute irure dolor in reprehenderit in voluptate velit esse cillum dolore eu fugiat nulla pariatur. Excepteur sint occaecat cupidatat non proident, sunt in culpa qui officia deserunt mollit anim id est laborum.</p>
    </section>

    <section class="sign-off">
      <div class="signature" role="img" aria-label="Handwritten signature of the attorney in blue ink"></div>
      <div class="sign-off__text">
        Yours Sincerely,<br>
        <span class="sign-off__name">Dara Ellison</span>
      </div>
    </section>

    <footer class="footer">
      <div class="footer__firm">Pell &amp; Whitcombe, Attorneys-At-Law, LLP</div>
      <div class="footer__contact">1840 W Rosedale Ave, Fort Worth, Texas 76104-2218. <b>Phone:</b> (817) 555-0147 &nbsp;<b>Fax:</b> (817) 555-0148</div>
      <div class="footer__rule"></div>
    </footer>
  </article>
</main>
</body>
</html>
```